Personal Tax Specialists Banner

We need banner adverts for a personal tax firm. We specialise in Luxembourg, US and UK personal taxation. The banner should be modern, cool, simple and illustrated.

Banner should highlight "Personal Taxation Specialists" and the countries that we specialise in, "Luxembourg", "US" and "UK".

Target Market(s)

Individuals looking for assistance with tax return preparation.

Industry/Entity Type

Finance And Accounting

Colors

Designer to choose colors to be used in the design.

Requirements
Must have
• Output in GIF.
• The main banner size is 980 x 120 and some smaller square banners (300 x 300)
• Button to link back to website www.quendrifin.com
Nice to have
• We would like an illustrated design if possible.

```html
<!DOCTYPE html>
<html lang="en">
<head>
<meta charset="utf-8">
<title>Quendri Tax &amp; Consulting – Banners</title>
<link rel="stylesheet" href="https://fonts.googleapis.com/css2?family=Nunito:wght@800&family=Roboto:wght@400&display=swap">
<style>
  :root {
    --maroon: #780032;
    --maroon-text: #7a1238;
    --grey-edge: #8a8a8c;
    --white: #ffffff;
    --gold: #a8740f;
    --frame: #2a2a2a;
    --art-light: #f1eeee;
    --art-mid: #d6d0d3;
    --art-deep: #b9b1b5;
  }
  * { box-sizing: border-box; margin: 0; padding: 0; }
  html, body { width: 1200px; height: 508px; overflow: hidden; background: var(--white); }
  .stage {
    position: relative;
    width: 1000px;
    height: 423.4px;
    transform: scale(1.2);
    transform-origin: 0 0;
  }
  .banner {
    position: absolute;
    left: 15px;
    width: 980px;
    height: 120px;
    background: var(--maroon);
    border: 1px solid var(--frame);
    overflow: hidden;
  }
  .banner--one { top: 13px; }
  .banner--two { top: 152px; }
  .banner--three { top: 291px; }

  .brand-panel { position: absolute; left: 0; top: 0; width: 300px; height: 118px; }
  .brand {
    position: absolute;
    left: 24px;
    top: 33px;
    display: flex;
    align-items: center;
    gap: 14px;
    color: var(--maroon-text);
    font-family: "Roboto", Arial, sans-serif;
    font-weight: 400;
  }
  .brand-dot {
    width: 50px; height: 50px;
    border-radius: 50%;
    background: var(--maroon-text);
  }
  .brand-name { line-height: 1; }
  .brand-name .line-main { display: block; font-size: 33px; letter-spacing: 0.5px; }
  .brand-name .line-sub { display: block; font-size: 15px; margin-top: 3px; letter-spacing: 0.3px; }

  .headline {
    position: absolute;
    left: 304px;
    width: 280px;
    top: 0;
    height: 118px;
    display: flex;
    align-items: center;
    justify-content: center;
    text-align: center;
    color: var(--white);
    font-family: "Nunito", "Arial Rounded MT Bold", sans-serif;
    font-weight: 800;
    font-size: 25px;
    line-height: 1.18;
  }

  .artwork {
    position: absolute;
    left: 588px;
    top: 8px;
    width: 232px;
    height: 104px;
    border-radius: 8px;
    background: linear-gradient(160deg, var(--art-light) 0%, var(--art-mid) 60%, var(--art-deep) 100%);
  }

  .cta {
    position: absolute;
    left: 821px;
    top: 43px;
    width: 146px;
    height: 37px;
    display: flex;
    align-items: center;
    justify-content: center;
    background: var(--gold);
    border: 1px solid var(--white);
    box-shadow: 2px 2px 0 rgba(0,0,0,0.35);
    color: var(--white);
    font-family: "Roboto", Arial, sans-serif;
    font-size: 16px;
    text-decoration: none;
  }
</style>
</head>
<body>
<main class="stage">

  <section class="banner banner--one">
    <svg class="brand-panel" viewBox="0 0 300 118" aria-hidden="true">
      <path d="M0 0 H284 Q296 50 294 118 H0 Z" fill="var(--grey-edge)"/>
      <path d="M0 0 H272 Q285 50 282 118 H0 Z" fill="var(--white)"/>
    </svg>
    <div class="brand">
      <span class="brand-dot"></span>
      <span class="brand-name"><span class="line-main">QUENDRI</span><span class="line-sub">TAX &amp; CONSULTING</span></span>
    </div>
    <h2 class="headline">Personal Taxation<br>Specialists</h2>
    <div class="artwork" role="img" aria-label="Hand-lettered word TAX being chalked by a hand"></div>
    <a class="cta" href="https://www.quendrifin.com">Learn More</a>
  </section>

  <section class="banner banner--two">
    <svg class="brand-panel" viewBox="0 0 300 118" aria-hidden="true">
      <path d="M0 0 H284 Q296 50 294 118 H0 Z" fill="var(--grey-edge)"/>
      <path d="M0 0 H272 Q285 50 282 118 H0 Z" fill="var(--white)"/>
    </svg>
    <div class="brand">
      <span class="brand-dot"></span>
      <span class="brand-name"><span class="line-main">QUENDRI</span><span class="line-sub">TAX &amp; CONSULTING</span></span>
    </div>
    <h2 class="headline">Personal Taxation<br>Specialists</h2>
    <div class="artwork" role="img" aria-label="Hand-lettered word TAX underlined by a hand with chalk"></div>
    <a class="cta" href="https://www.quendrifin.com">Learn More</a>
  </section>

  <section class="banner banner--three">
    <svg class="brand-panel" viewBox="0 0 300 118" aria-hidden="true">
      <path d="M0 0 H284 Q296 50 294 118 H0 Z" fill="var(--grey-edge)"/>
      <path d="M0 0 H272 Q285 50 282 118 H0 Z" fill="var(--white)"/>
    </svg>
    <div class="brand">
      <span class="brand-dot"></span>
      <span class="brand-name"><span class="line-main">QUENDRI</span><span class="line-sub">TAX &amp; CONSULTING</span></span>
    </div>
    <h2 class="headline">In Luxembourg,<br>US and UK</h2>
    <div class="artwork" role="img" aria-label="Hand-lettered word TAX underlined by a hand with chalk"></div>
    <a class="cta" href="https://www.quendrifin.com">Learn More</a>
  </section>

</main>
</body>
</html>
```